Banner Ad Design Project for Home Technology Company

We need banner ads designed for our company. See the description of what we do below the basic messages listed, section titled "ABOUT LANTERNWAY"

Basic Messages:
See it. Hear it. Live it.

1. Message #1: Discover YOUR Lanternway. Audio? Video? Media Rooms? Connected Home? We do it all!

2. Message #2: Audio
You don't need magical ears to find the perfect speakers. It's as simple as: "Which speakers sound best to you?" We can help, but it's ultimately your decision.

3. Message #3: Digital Media
- Option A: The future of how we listen to music is happening now.
- Option B: Are you just listening to your music or are you enjoying it?
- Option C: Take control of your music.
- Option D: If you aren't blown away, we aren't doing our job!

4. Message #4: Media Room
It doesn't matter where you want to watch TV & movies, enjoy your favorite music, or host parties where your guests get to be the DJ, we can help you create your ultimate entertainment zone. We've created numerous media rooms, dedicated home theaters, game rooms, and whole home entertainment systems.

5. Message #5: Connected Home
Enhance your home and your life.

ABOUT LANTERNWAY:
Technology is everywhere. It’s hard to imagine any aspect of our lives that doesn’t involve it. From phones to our cars, from work to our home, technology enhances our lives, bringing us closer to information, entertainment, and each other. Often though, our different devices exist in isolation, connecting us to the world, but rarely working together to create a more elegant whole. It doesn’t have to be that way.

Imagine a home that greets you by unlocking the front door, disabling the security system, turning on lights, and welcoming you with your favorite music. Imagine a home that automatically lowers shades before the sun can fade your furniture and décor. Imagine a favorite song playing in each room of the house, or the latest hit film streaming and displayed across a wall-sized screen. Imagine prompting all of this from your smart phone.

This is only the beginning of the promise offered by an intelligent home. Beyond showcasing the latest technology, the ultimate goal is to make interaction with your home’s advanced automation features a pleasure. Exceptionally easy, yet wonderfully sophisticated, it is technology designed to help you manage your life.It’s about living in the home of the future, right now.

Here at Lanternway we’ve helped families make complex technology simple for over 36 years. We provide advanced, professional, creative resources dedicated to ensuring your project’s success. From beautifully integrated design to the finest home technologies, we’ll guide you through each step of the design and installation process to make certain you have exactly the products you need, the features you want, and the personal attention that will make the home of the future a joy to own today.

Enhance your home and your life; let us show you how.
Updates

Brief will be completed soon. Please wait until that has been posted.  I'm setting up projects now, then adding the creative briefs.

Thank you for your patience.

Brief has been updated & Lots of information has been added.

Project Deadline Extended

Added a file with some lifestyle photos of products we sell. If you need others, please make a request.

Some lifestyle product photos of products we sell can be downloaded from this link: http://lnk.example/Xq7P

We are still looking for more designs. While we've found a few that we do like, we're still looking for more.  That's why we've extended the deadline by another week.  Please continue to submit designs as all will be considered.

Target Market(s)

English-speaking adults, aged 35-55. 60% are married; 40% have children in the household. 75% have college degrees or greater. These are innovation seekers, design & technology enthusiasts. They're interested in having premium experiences, top brands, being the first to own the latest and greatest in technology.

Industry/Entity Type

Entertainment

Requirements
Must have
- Must include only one message per banner ad set.
- Must mimic the current design style of lanternway.example.
- Please make sure that each individual banners file size is less than 40k
Nice to have
• Button that allows viewers to click through to our website. Button should include text such as:
- Learn More
- Discover More

The above are purely examples; other calls-to-action could also work.
Should not have
• Curved Lines.

```html
<!DOCTYPE html>
<html lang="en">
<head>
<meta charset="utf-8">
<title>Lanternway banner set</title>
<link rel="stylesheet" href="https://fonts.googleapis.com/css2?family=Fira+Sans:wght@400;500&display=swap">
<style>
  :root {
    --stage: #ece8e3;
    --panel-dark: #111111;
    --panel-ray: #1d1d1d;
    --paper: #ffffff;
    --gold: #f2a81d;
    --gold-text: #f5ad1f;
    --btn-top: #ffd83a;
    --btn-bottom: #f2b000;
    --ink: #2a2a2a;
    --light: #ffffff;
    --horn-a: #6c6a64;
    --horn-b: #2e2418;
  }
  * { box-sizing: border-box; margin: 0; padding: 0; }
  html, body { width: 1200px; height: 761px; overflow: hidden; }
  body {
    background: var(--stage);
    font-family: "Fira Sans", sans-serif;
    position: relative;
  }
  .banner {
    position: absolute;
    overflow: hidden;
    background: radial-gradient(ellipse at 60% 100%, var(--panel-ray), var(--panel-dark) 70%);
    box-shadow: 0 3px 8px rgba(0,0,0,.35);
    color: var(--light);
  }
  .banner > * { position: absolute; }
  .masthead { left: 0; top: 0; }
  .brand-name { color: var(--ink); font-weight: 400; letter-spacing: -0.02em; white-space: nowrap; }
  .brand-dot { border-radius: 50%; background: var(--gold); }
  .tagline { color: var(--ink); white-space: nowrap; }
  .headline { line-height: 1.12; white-space: nowrap; }
  .questions { color: var(--gold-text); line-height: 1.2; white-space: nowrap; }
  .closer { white-space: nowrap; }
  .cta {
    display: flex; align-items: center; justify-content: center;
    background: linear-gradient(var(--btn-top), var(--btn-bottom));
    color: #1a1a1a; border-radius: 3px; font-weight: 500;
    box-shadow: 0 1px 2px rgba(0,0,0,.5);
  }
  .product-art {
    background: radial-gradient(ellipse at 35% 35%, var(--horn-a), var(--horn-b) 70%, transparent 72%);
  }

  /* Skyscraper */
  .sky { left: 61px; top: 67px; width: 179px; height: 669px; }
  .sky .brand-dot { left: 22px; top: 38px; width: 14px; height: 14px; }
  .sky .brand-name { left: 40px; top: 32px; font-size: 20px; }
  .sky .tagline { left: 0; width: 179px; text-align: center; top: 112px; font-size: 15px; }
  .sky .headline { left: 0; width: 179px; text-align: center; top: 188px; font-size: 23px; }
  .sky .headline .big { font-size: 28px; }
  .sky .questions { left: 0; width: 179px; text-align: center; top: 268px; font-size: 21px; }
  .sky .closer { left: 0; width: 179px; text-align: center; top: 477px; font-size: 27px; }
  .sky .product-art { left: 18px; top: 452px; width: 150px; height: 162px; }
  .sky .cta { left: 17px; top: 625px; width: 138px; height: 31px; font-size: 16px; }

  /* Medium rectangle */
  .rect { left: 273px; top: 67px; width: 375px; height: 312px; }
  .rect .brand-dot { left: 14px; top: 74px; width: 12px; height: 12px; }
  .rect .brand-name { left: 30px; top: 67px; font-size: 19px; }
  .rect .tagline { left: 12px; top: 98px; font-size: 14px; }
  .rect .headline { left: 12px; top: 144px; font-size: 24px; }
  .rect .headline .big { font-size: 28px; }
  .rect .questions { left: 12px; top: 221px; font-size: 18px; }
  .rect .closer { left: 12px; top: 275px; font-size: 23px; }
  .rect .product-art { left: 175px; top: 0; width: 200px; height: 225px; }
  .rect .cta { left: 216px; top: 264px; width: 139px; height: 31px; font-size: 17px; }

  /* Small rectangle */
  .rect-sm { left: 691px; top: 67px; width: 335px; height: 279px; }
  .rect-sm .brand-dot { left: 10px; top: 65px; width: 11px; height: 11px; }
  .rect-sm .brand-name { left: 25px; top: 59px; font-size: 17px; }
  .rect-sm .tagline { left: 10px; top: 86px; font-size: 13px; }
  .rect-sm .headline { left: 10px; top: 129px; font-size: 22px; }
  .rect-sm .headline .big { font-size: 25px; }
  .rect-sm .questions { left: 10px; top: 197px; font-size: 16px; }
  .rect-sm .closer { left: 10px; top: 246px; font-size: 21px; }
  .rect-sm .product-art { left: 160px; top: 0; width: 175px; height: 200px; }
  .rect-sm .cta { left: 193px; top: 236px; width: 124px; height: 28px; font-size: 15px; }

  /* Small leaderboard */
  .board-sm { left: 285px; top: 485px; width: 521px; height: 65px; }
  .board-sm .brand-dot { left: 5px; top: 30px; width: 7px; height: 7px; }
  .board-sm .brand-name { left: 14px; top: 27px; font-size: 11px; }
  .board-sm .tagline { left: 5px; top: 49px; font-size: 8px; }
  .board-sm .headline { left: 122px; top: 6px; font-size: 16px; }
  .board-sm .questions { left: 122px; top: 28px; width: 215px; text-align: center; font-size: 12px; line-height: 1.35; }
  .board-sm .product-art { left: 340px; top: 4px; width: 60px; height: 56px; }
  .board-sm .closer { left: 416px; top: 9px; font-size: 15px; }
  .board-sm .cta { left: 416px; top: 33px; width: 90px; height: 20px; font-size: 11px; }

  /* Leaderboard */
  .board { left: 285px; top: 574px; width: 812px; height: 100px; }
  .board .brand-dot { left: 8px; top: 47px; width: 10px; height: 10px; }
  .board .brand-name { left: 22px; top: 41px; font-size: 17px; }
  .board .tagline { left: 11px; top: 78px; font-size: 13px; }
  .board .headline { left: 190px; top: 10px; width: 310px; text-align: center; font-size: 26px; }
  .board .questions { left: 190px; top: 43px; width: 310px; text-align: center; font-size: 19px; }
  .board .product-art { left: 530px; top: 4px; width: 82px; height: 86px; }
  .board .closer { left: 645px; top: 15px; width: 150px; text-align: center; font-size: 24px; }
  .board .cta { left: 647px; top: 52px; width: 138px; height: 31px; font-size: 17px; }
</style>
</head>
<body>

<section class="banner sky" aria-label="Skyscraper banner">
  <svg class="masthead" width="179" height="175" viewBox="0 0 179 175" aria-hidden="true">
    <path d="M0 0H179V138Q90 132 0 158Z" fill="var(--paper)"/>
    <path d="M0 158Q90 132 179 138V148Q90 142 0 168Z" fill="var(--gold)"/>
  </svg>
  <span class="brand-dot"></span>
  <span class="brand-name">LANTERNWAY</span>
  <p class="tagline">See it. Hear it. Live it.</p>
  <h2 class="headline">Discover YOUR<br><span class="big">Lanternway</span></h2>
  <p class="questions">Audio?<br>Video?<br>Media Rooms?<br>Connected<br>Home?</p>
  <p class="closer">We do it all!</p>
  <div class="product-art" role="img" aria-label="Vintage horn gramophone on a wooden cabinet"></div>
  <a class="cta">Learn More!</a>
</section>

<section class="banner rect" aria-label="Medium rectangle banner">
  <svg class="masthead" width="375" height="180" viewBox="0 0 375 180" aria-hidden="true">
    <path d="M0 0H230V110Q120 108 0 122Z" fill="var(--paper)"/>
    <path d="M0 122Q120 108 230 110V118Q120 116 0 130Z" fill="var(--gold)"/>
  </svg>
  <span class="brand-dot"></span>
  <span class="brand-name">LANTERNWAY</span>
  <p class="tagline">See it. Hear it. Live it.</p>
  <div class="product-art" role="img" aria-label="Vintage horn gramophone on a wooden cabinet"></div>
  <h2 class="headline">Discover YOUR<br><span class="big">Lanternway</span></h2>
  <p class="questions">Audio? Video? Media Rooms?<br>Connected Home?</p>
  <p class="closer">We do it all!</p>
  <a class="cta">Learn More!</a>
</section>

<section class="banner rect-sm" aria-label="Small rectangle banner">
  <svg class="masthead" width="335" height="120" viewBox="0 0 335 120" aria-hidden="true">
    <path d="M0 0H200V96Q100 94 0 106Z" fill="var(--paper)"/>
    <path d="M0 106Q100 94 200 96V103Q100 101 0 113Z" fill="var(--gold)"/>
  </svg>
  <span class="brand-dot"></span>
  <span class="brand-name">LANTERNWAY</span>
  <p class="tagline">See it. Hear it. Live it.</p>
  <div class="product-art" role="img" aria-label="Vintage horn gramophone on a wooden cabinet"></div>
  <h2 class="headline">Discover YOUR<br><span class="big">Lanternway</span></h2>
  <p class="questions">Audio? Video? Media Rooms?<br>Connected Home?</p>
  <p class="closer">We do it all!</p>
  <a class="cta">Learn More!</a>
</section>

<section class="banner board-sm" aria-label="Small leaderboard banner">
  <svg class="masthead" width="120" height="65" viewBox="0 0 120 65" aria-hidden="true">
    <path d="M0 0H104Q96 32 104 65H0Z" fill="var(--paper)"/>
    <path d="M104 0H110Q102 32 110 65H104Q96 32 104 0Z" fill="var(--gold)"/>
  </svg>
  <span class="brand-dot"></span>
  <span class="brand-name">LANTERNWAY</span>
  <p class="tagline">See it. Hear it. Live it.</p>
  <h2 class="headline">Discover YOUR Lanternway</h2>
  <p class="questions">Audio? Video? Media Rooms?<br>Connected Home?</p>
  <div class="product-art" role="img" aria-label="Vintage horn gramophone"></div>
  <p class="closer">We do it all!</p>
  <a class="cta">Learn More!</a>
</section>

<section class="banner board" aria-label="Leaderboard banner">
  <svg class="masthead" width="175" height="100" viewBox="0 0 175 100" aria-hidden="true">
    <path d="M0 0H150Q136 50 150 100H0Z" fill="var(--paper)"/>
    <path d="M150 0H160Q146 50 160 100H150Q136 50 150 0Z" fill="var(--gold)"/>
  </svg>
  <span class="brand-dot"></span>
  <span class="brand-name">LANTERNWAY</span>
  <p class="tagline">See it. Hear it. Live it.</p>
  <h2 class="headline">Discover YOUR Lanternway</h2>
  <p class="questions">Audio? Video? Media Rooms?<br>Connected Home?</p>
  <div class="product-art" role="img" aria-label="Vintage horn gramophone on a wooden cabinet"></div>
  <p class="closer">We do it all!</p>
  <a class="cta">Learn More!</a>
</section>

</body>
</html>
```